Larkspur Ridge Management - Business Cards

I need business cards. My current logo was designed by a designer at this site and I very much like and am happy with the results. I would like a business card that is trendy, unique, current yet professional. I deal with high net worth clients daily

Target Market(s)

Out of state investors looking to get into the rental market in Ohio

Industry/Entity Type

Property Management, Consulting

Contact Information for Business Card

Name, Title (Chief Financial Officer) office phone number (555) 817-3094 website address larkridgemgmt.example

Font styles to use
Sans Serif

Colors
0054AA
0677BA
7BADD7
CADEEF
E8F1F8
0094D4
00A9DD
6FCCEA
C7EBF8
E9F6FB
00AB8E
00BBA5
67D7C9
C6EFE9
E9F9F6

```html
<!DOCTYPE html>
<html lang="en">
<head>
<meta charset="utf-8">
<title>Larkspur Ridge Management – Business Cards</title>
<link rel="stylesheet" href="https://fonts.googleapis.com/css2?family=Montserrat:wght@500;600;700;800&display=swap">
<style>
  :root {
    --brand-blue: #0054AA;
    --deep-blue: #00468f;
    --teal: #00BBA5;
    --teal-light: #67D7C9;
    --sky-tint: #E8F1F8;
    --white: #ffffff;
    --backdrop: #ced3d6;
    --font: "Montserrat", sans-serif;
  }
  * { margin: 0; padding: 0; box-sizing: border-box; }
  html, body {
    width: 1200px; height: 900px; overflow: hidden;
    background: var(--backdrop);
    font-family: var(--font);
  }
  .stage { position: relative; width: 1200px; height: 900px; }
  .card {
    position: absolute; top: 115px;
    width: 387px; height: 671px;
    background: var(--white); overflow: hidden;
  }
  .card--front { left: 180px; }
  .card--back { left: 636px; }

  .wordmark {
    position: absolute; left: 0; right: 0;
    text-align: center; color: var(--brand-blue);
    font-weight: 800; text-transform: uppercase;
    line-height: 1.08;
  }
  .card--front .wordmark { top: 272px; font-size: 38px; letter-spacing: 1px; }
  .card--back .wordmark { top: 96px; font-size: 32px; letter-spacing: 1px; }

  .back-field { position: absolute; inset: 0; }

  .holder {
    position: absolute; left: 0; right: 0; top: 410px;
    text-align: center;
  }
  .holder__name {
    color: var(--teal-light); font-weight: 800; font-size: 25px;
    line-height: 32px; letter-spacing: 1px; text-transform: uppercase;
  }
  .holder__title {
    color: var(--white); font-weight: 600; font-size: 17px;
    letter-spacing: 0.6px; margin-top: 2px;
  }
  .contact-icons {
    position: absolute; top: 510px; left: 0; right: 0;
    display: flex; justify-content: center; gap: 10px;
  }
  .contact-list {
    position: absolute; left: 33px; right: 30px; top: 546px;
    list-style: none; color: var(--white);
  }
  .contact-list li { font-weight: 500; white-space: nowrap; }
  .contact-list .phone { font-size: 19.5px; line-height: 32px; }
  .contact-list .email { font-size: 16.5px; line-height: 27px; }
  .contact-list .web { font-size: 18.5px; line-height: 32px; letter-spacing: 0.4px; }
</style>
</head>
<body>
<main class="stage">

  <section class="card card--front" aria-label="Card front">
    <p class="wordmark">Larkspur<br>Ridge<br>Management</p>
  </section>

  <section class="card card--back" aria-label="Card back">
    <svg class="back-field" width="387" height="671" viewBox="0 0 387 671" aria-hidden="true">
      <defs>
        <linearGradient id="field-blue" x1="0" y1="0" x2="0" y2="1">
          <stop offset="0" stop-color="var(--brand-blue)"/>
          <stop offset="1" stop-color="var(--deep-blue)"/>
        </linearGradient>
      </defs>
      <polygon points="0,265 193.5,380 387,265 387,671 0,671" fill="var(--teal)"/>
      <polygon points="0,273 193.5,388 387,273 387,671 0,671" fill="url(#field-blue)"/>
    </svg>

    <p class="wordmark">Larkspur<br>Ridge<br>Management</p>

    <div class="holder">
      <p class="holder__name">Marco Elias<br>Varela</p>
      <p class="holder__title">Chief Financial Officer</p>
    </div>

    <div class="contact-icons" aria-hidden="true">
      <svg width="20" height="20" viewBox="0 0 24 24">
        <path fill="var(--teal-light)" d="M6.6 10.8a15.1 15.1 0 0 0 6.6 6.6l2.2-2.2a1 1 0 0 1 1-.25 11.4 11.4 0 0 0 3.6.57 1 1 0 0 1 1 1V20a1 1 0 0 1-1 1A17 17 0 0 1 3 4a1 1 0 0 1 1-1h3.5a1 1 0 0 1 1 1c0 1.25.2 2.45.57 3.57a1 1 0 0 1-.25 1z"/>
      </svg>
      <svg width="20" height="20" viewBox="0 0 24 24">
        <rect x="2" y="5" width="20" height="14" fill="var(--teal-light)"/>
        <path d="M2 5l10 8 10-8" fill="none" stroke="var(--brand-blue)" stroke-width="1.6"/>
      </svg>
      <svg width="20" height="20" viewBox="0 0 24 24" fill="none" stroke="var(--teal-light)" stroke-width="1.8">
        <circle cx="12" cy="12" r="9.5"/>
        <ellipse cx="12" cy="12" rx="4" ry="9.5"/>
        <line x1="2.5" y1="12" x2="21.5" y2="12"/>
        <line x1="12" y1="2.5" x2="12" y2="21.5"/>
      </svg>
    </div>

    <ul class="contact-list">
      <li class="phone">+1 (555) 817-3094 Office Call/Text</li>
      <li class="email">info@larkridgemgmt.example</li>
      <li class="web">larkridgemgmt.example</li>
    </ul>
  </section>

</main>
</body>
</html>
```